Website-Design für die neue Handtaschenmarke Marvona
Zielgruppe
Frauen und auch Männer, die ästhetisch ausgearbeitete und gleichzeitig zweckmäßige Handtaschen und Accessoires suchen. Frauen, die Einzelstücke nach ihren Wünschen und Bedürfnissen angefertigt haben wollen.
Aufgabenstellung
Es soll die Startseite für eine Website mit einem kleinen angebundenen Online-Shop entstehen.
Es gibt keine bestehende Website, nur das Logo steht fest.
Das detailierte Briefing finden Sie als PDF Dokument in der Anlage.

```html
<!DOCTYPE html>
<html lang="de">
<head>
<meta charset="utf-8">
<title>Marvona – Startseite</title>
<link rel="stylesheet" href="https://fonts.googleapis.com/css2?family=Arimo:wght@400&family=Tenor+Sans&display=swap">
<style>
  :root {
    --page-bg: #ffffff;
    --frame-border: #bdbdbd;
    --frame-shadow: #6b6b6b;
    --ink: #111111;
    --hero-sky: #efefed;
    --hero-haze: #e2e0dc;
    --hero-shirt: #cdc8c1;
    --hero-skin: #a89585;
    --hero-leather: #7b6554;
    --hero-shadow: #3f352e;
    --hero-border: #b5b5b5;
  }
  * { margin: 0; padding: 0; box-sizing: border-box; }
  html, body {
    width: 1200px;
    height: 848px;
    overflow: hidden;
    background: var(--page-bg);
    font-family: "Arimo", Arial, sans-serif;
    color: var(--ink);
  }
  .site-frame {
    position: absolute;
    left: 32px;
    top: 113px;
    width: 1123px;
    height: 601px;
    background: var(--page-bg);
    border: 1px solid var(--frame-border);
    box-shadow: 11px 11px 6px var(--frame-shadow);
  }
  .brand-name {
    position: absolute;
    left: 33px;
    top: 37px;
    font-family: "Tenor Sans", "Optima", sans-serif;
    font-size: 19px;
    letter-spacing: 0.8px;
    line-height: 1;
  }
  .brand-mark {
    position: absolute;
    right: 217px;
    top: 46px;
    display: flex;
    align-items: center;
    gap: 7px;
    font-family: "Tenor Sans", "Optima", sans-serif;
    font-size: 13px;
    letter-spacing: 0.8px;
    line-height: 1;
  }
  .brand-mark .mark-dot {
    width: 14px;
    height: 14px;
    border: 1.5px solid var(--ink);
    border-radius: 50%;
  }
  .main-nav {
    position: absolute;
    left: 33px;
    top: 116px;
    width: 873px;
    display: flex;
    font-size: 12.5px;
    line-height: 14px;
  }
  .main-nav a, .footer-nav a { color: var(--ink); text-decoration: none; }
  .main-nav a { margin-right: 22px; }
  .main-nav .shop-link { margin-left: auto; margin-right: 0; }
  .hero {
    position: absolute;
    left: 33px;
    top: 143px;
    width: 871px;
    height: 379px;
    border: 1px solid var(--hero-border);
    background:
      radial-gradient(ellipse 16% 30% at 24% 86%, var(--hero-leather), rgba(123,101,84,0) 100%),
      radial-gradient(ellipse 10% 28% at 36% 70%, var(--hero-shadow), rgba(63,53,46,0) 100%),
      radial-gradient(ellipse 9% 16% at 78% 25%, var(--hero-skin), rgba(168,149,133,0) 100%),
      radial-gradient(ellipse 14% 22% at 80% 85%, var(--hero-skin), rgba(168,149,133,0) 100%),
      radial-gradient(ellipse 34% 62% at 70% 70%, var(--hero-shirt), rgba(205,200,193,0) 100%),
      linear-gradient(90deg, var(--hero-sky) 0%, var(--hero-sky) 35%, var(--hero-haze) 60%, var(--hero-haze) 100%);
  }
  .footer-nav {
    position: absolute;
    left: 33px;
    top: 537px;
    display: flex;
    font-size: 12.5px;
    line-height: 14px;
  }
  .footer-nav a { margin-right: 21px; }
</style>
</head>
<body>
  <div class="site-frame">
    <header>
      <div class="brand-name">MARVONA</div>
      <div class="brand-mark"><span class="mark-dot"></span><span>MARVONA</span></div>
      <nav class="main-nav">
        <a href="#">UNTERNEHMEN</a>
        <a href="#">PRODUKTE</a>
        <a href="#">NEUHEITEN</a>
        <a href="#">INDIVUAL SERVICE</a>
        <a href="#">KONTAKT</a>
        <a href="#" class="shop-link">&gt;&gt; SHOP</a>
      </nav>
    </header>
    <main>
      <div class="hero" role="img" aria-label="Schwarzweiß-Foto: Frau in gestreifter Bluse mit brauner Ledertasche über der Schulter vor hellem Hintergrund"></div>
    </main>
    <footer class="footer-nav">
      <a href="#">IMPRESSUM</a>
      <a href="#">AGB</a>
      <a href="#">BLOG</a>
      <a href="#">FRIENDLA</a>
    </footer>
  </div>
</body>
</html>
```